Landing page design for secure cloud backup web application

We would like a landing page design for our web application. Our app allows users to securely save their data in the cloud using their existing storage providers, such as stashPod, Pila, Ferravex Haze Locker, Quorble vault and Tandrix Pax vault.
We make it extremely easy for individual users and small businesses to deploy sophisticated client-side encryption without having to worry about the technical complexity inherent in such solutions.
We already have the logo design done - I am attaching the logo file. We also have a preliminary website drafted at www.plimva.com
I need a good color scheme, typography, layout, along with templates for 'help', 'about', 'privacy notice', 'legal' and such typical sub-pages
The design should be uncluttered, clean and minimalist

Target Market(s)

Individuals and medium/small businesses that are conscious about the security of their data in the cloud

Coding

Coded - Design and coding required

Number of Pages Required

4 page

Font styles to use
Sans Serif

Requirements
Must have
• Section where I describe the product along with pictures/images
• section for explainer video on main page
• FAQ section
• Help section
• Legal/privacynotice/terms of use section
• feedback section
Nice to have
• see existing draft site www.plimva.com for content guidelines only.
• see attached logo files for color scheme guidelines - I am willing to accept change in the logo color if necessary to create a better web site look and feel
• Fonts on page should match font in the logo

```html
<!DOCTYPE html>
<html lang="en">
<head>
<meta charset="utf-8">
<title>Plimva – Secure Cloud Storage</title>
<link rel="stylesheet" href="https://fonts.googleapis.com/css2?family=Arimo:wght@400;700&family=Open+Sans:wght@300;400&family=Courier+Prime&display=swap">
<style>
:root{
  --orange:#f5961f;
  --orange-deep:#ef8a12;
  --header:#4f4f4f;
  --contact:#6b6b6b;
  --ink:#3a3a3a;
  --muted:#5a5a5a;
  --soft:#eeeeee;
  --paper:#f7f7f7;
  --white:#ffffff;
}
*{box-sizing:border-box;margin:0;padding:0}
html,body{width:1200px;height:3766px;overflow:hidden}
body{position:relative;background:var(--white);font-family:"Arimo",Arial,sans-serif;color:var(--ink)}
.abs{position:absolute}

/* header */
.site-header{left:0;top:0;width:1200px;height:88px;background:var(--header);border-top:8px solid var(--orange)}
.brand{left:48px;top:20px;display:flex;align-items:center;gap:10px;color:var(--white);font-size:34px;font-weight:700}
.brand-dot{width:30px;height:30px;border-radius:50%;background:var(--orange)}
.nav{top:34px;left:0;width:900px;height:20px}
.nav a{position:absolute;color:var(--white);text-decoration:none;font-size:15px;white-space:nowrap}
.nav a.active{border-bottom:3px solid var(--orange);padding-bottom:8px}
.signup{left:956px;top:30px;width:200px;height:42px;background:#6a6a6a;border:1px solid #8a8a8a;color:var(--white);font-size:15px;display:flex;align-items:center;justify-content:center}

/* welcome */
.welcome{left:0;top:88px;width:1200px;height:552px;background:var(--soft)}
.welcome h1{position:absolute;left:0;top:130px;width:1200px;text-align:center;font-size:70px;font-weight:700;color:#555}
.welcome .intro{position:absolute;left:60px;top:236px;width:1080px;text-align:center;font-size:16px;line-height:22px;color:var(--muted)}
.welcome h2{position:absolute;left:0;top:352px;width:1200px;text-align:center;font-family:"Open Sans",sans-serif;font-weight:300;font-size:42px;color:#444}
.welcome .vision{position:absolute;left:0;top:440px;width:1200px;text-align:center;font-size:16px;color:var(--muted)}
.pointer{left:580px;top:640px;width:0;height:0;border-left:20px solid transparent;border-right:20px solid transparent;border-top:18px solid var(--soft);z-index:2}

/* showcase */
.showcase{left:0;top:640px;width:1200px;height:808px;background:var(--orange)}
.app-preview{left:83px;top:38px;width:1037px;height:590px;border-radius:18px 18px 6px 6px;background:linear-gradient(#2c2c2c 0 4%,#f4ecd3 4% 92%,#3a3a3a 92%);}
.showcase h3{position:absolute;left:0;top:712px;width:1200px;text-align:center;color:var(--white);font-size:26px;font-weight:700}

/* features */
.features{left:0;top:1448px;width:1200px;height:760px;background:var(--white)}
.feature{width:320px;text-align:center}
.feature-icon{display:block;margin:0 auto 26px}
.feature h4{font-size:16px;font-weight:700;color:#333;margin-bottom:14px}
.feature p{font-size:13px;line-height:17px;color:var(--muted)}
.feature .link{color:var(--orange-deep)}
.divider{left:40px;top:360px;width:760px;height:1px;background:#e2e2e2}

/* faq */
.faq{left:0;top:2208px;width:1200px;height:867px;background:var(--paper)}
.faq-band{left:0;top:0;width:1200px;height:190px;background:linear-gradient(#e4e4e4,#f4f4f4)}
.faq h2{position:absolute;left:0;top:58px;width:1200px;text-align:center;font-size:64px;font-weight:700;color:#666}
.faq-item{left:48px;width:1110px;font-family:"Courier Prime",monospace;color:var(--ink)}
.faq-item h3{font-size:26px;font-weight:400;margin-bottom:8px}
.faq-item p{font-size:13.5px;line-height:19px;color:#555}
.read-more{left:502px;top:744px;width:196px;height:36px;background:#8c8c8c;color:var(--white);font-size:17px;display:flex;align-items:center;justify-content:center}

/* developers */
.developers{left:0;top:3075px;width:1200px;height:271px;background:var(--orange);color:var(--white);text-align:center}
.developers h2{position:absolute;top:56px;width:1200px;font-size:28px;font-weight:700}
.developers p{position:absolute;left:60px;top:126px;width:1080px;font-size:15px;line-height:22px}

/* contact */
.contact{left:0;top:3346px;width:1200px;height:420px;background:var(--contact);color:var(--white)}
.contact h2{position:absolute;top:44px;width:1200px;text-align:center;font-size:28px;font-weight:700}
.contact .about{position:absolute;left:48px;top:118px;width:520px;font-size:14px;line-height:18px}
.social{top:194px;width:46px;height:46px;background:#8d8d8d;border-radius:4px}
.field{left:612px;width:300px;height:30px;background:#f4f4f4;color:#999;font-size:14px;padding:6px 8px}
.message{left:926px;top:118px;width:240px;height:124px;background:#f4f4f4;color:#999;font-size:14px;padding:6px 8px}
.send{left:1052px;top:254px;width:113px;height:28px;background:var(--orange);color:var(--white);font-size:14px;display:flex;align-items:center;justify-content:center}
.footer-rule{left:48px;top:299px;width:1104px;height:1px;background:#888}
.copyright{top:356px;width:1200px;text-align:center;font-size:14px;color:#c9c9c9}
</style>
</head>
<body>

<header class="abs site-header">
  <div class="abs brand"><span class="brand-dot"></span>Plimva</div>
  <nav class="abs nav">
    <a class="active" style="left:345px">HOME</a>
    <a style="left:428px">ABOUT</a>
    <a style="left:513px">FAQ</a>
    <a style="left:576px">HELP</a>
    <a style="left:650px">PRIVACY NOTICE</a>
    <a style="left:800px">FEEDBACK</a>
  </nav>
  <div class="abs signup">SIGN UP FREE</div>
</header>

<section class="abs welcome">
  <h1>Wellcome to Plimva!</h1>
  <p class="intro">You have data you want to keep to yourself. You want it safe in the cloud so you can get at it anywhere. You don't want to mess with encryption keys yet you want to keep hackers and snoops out. You know it shouldn't be so hard.<br>You're right.</p>
  <h2>WE HAS A SIMPLE VISION</h2>
  <p class="vision">Your data belongs to you and no one else. We make it really easy to keep it that way.</p>
</section>
<div class="abs pointer"></div>

<section class="abs showcase">
  <div class="abs app-preview" role="img" aria-label="Laptop showing the Plimva Secure Storage file manager with connected storage providers"></div>
  <h3>KEEP YOUR DATA PRIVATE WITHOUT BREAKING A SWEAT</h3>
</section>

<section class="abs features">
  <div class="abs feature" style="left:58px;top:70px">
    <svg class="feature-icon" width="104" height="104" viewBox="0 0 104 104"><circle cx="52" cy="52" r="50" fill="#fff" stroke="#f5961f" stroke-width="2"/><path d="M34 60a9 9 0 0 1 3-17 14 14 0 0 1 27-3 10 10 0 0 1 4 20z" fill="#f5961f"/></svg>
    <h4>USE YOUR CLOUD</h4>
    <p>Plimva lets you use the accounts you you already have and trust, such as Pila, stashPod, Ferravex Haze Locker, Tandrix Pax vault and Quorble vault</p>
  </div>
  <div class="abs feature" style="left:430px;top:70px">
    <svg class="feature-icon" width="104" height="104" viewBox="0 0 104 104"><circle cx="52" cy="52" r="50" fill="#fff" stroke="#f5961f" stroke-width="2"/><path d="M34 60a9 9 0 0 1 3-17 14 14 0 0 1 27-3 10 10 0 0 1 4 20z" fill="#f5961f"/></svg>
    <h4>ZERO KNOWLEDGE</h4>
    <p>When it comes to data security, zero knowledge is a good thing.No one, including Plimva can decipher or read your data. Yet, if you forget your password, we can reset it so you will never lose your data.<br><span class="link">See our FAQ for details on how we achieve this.</span></p>
  </div>
  <div class="abs feature" style="left:806px;top:70px">
    <svg class="feature-icon" width="104" height="104" viewBox="0 0 104 104"><circle cx="52" cy="52" r="50" fill="#fff" stroke="#f5961f" stroke-width="2"/><path d="M47 30a4 4 0 0 1 8 0v16h10a5 5 0 0 1 5 5v10a12 12 0 0 1-12 12h-5a12 12 0 0 1-10-6l-6-10a3 3 0 0 1 5-4l5 5z" fill="#f5961f"/></svg>
    <h4>EASY TO USE</h4>
    <p>Plimva is completely browser based.<br>So there is no software to install,no updates to perform.<br>Just point your browser to a url and go.</p>
  </div>
  <div class="abs divider"></div>
  <div class="abs feature" style="left:58px;top:404px">
    <svg class="feature-icon" width="104" height="104" viewBox="0 0 104 104"><circle cx="52" cy="52" r="50" fill="#fff" stroke="#f5961f" stroke-width="2"/><g fill="none" stroke="#f5961f" stroke-width="3"><circle cx="52" cy="52" r="18"/><ellipse cx="52" cy="52" rx="8" ry="18"/><path d="M34 52h36M37 43h30M37 61h30"/></g></svg>
    <h4>ACCESS ANYWHERE</h4>
    <p>Your data is accessibe from<br>anywhere you can use a browser<br>and access the internet.</p>
  </div>
  <div class="abs feature" style="left:430px;top:404px">
    <svg class="feature-icon" width="104" height="104" viewBox="0 0 104 104"><circle cx="52" cy="52" r="50" fill="#fff" stroke="#f5961f" stroke-width="2"/><g fill="none" stroke="#f5961f" stroke-width="3"><rect x="33" y="34" width="34" height="24" rx="2"/><path d="M44 66h12M50 58v8"/><rect x="60" y="48" width="12" height="20" rx="2" fill="#fff"/></g></svg>
    <h4>MULTIPLE APPS</h4>
    <p>Plimva has multiple apps<br>that allow you handle your most sensitive<br>data with complete privacy and ease.<br>- Passwords<br>- Bitcoin<br>- Secure notes<br>- Data backups</p>
  </div>
</section>

<section class="abs faq">
  <div class="abs faq-band"></div>
  <h2>FAQ</h2>
  <div class="abs faq-item" style="top:250px">
    <h3>1 Where is my data stored?</h3>
    <p>Your data is stored on your accounts on two or more of the following storage providers - Pila, stashPod, Quorble vault, Tandrix Pax vault and Ferravex Haze Locker. Plimva does not provide storage. When you set up your account with Plimva, you will select the storage providers you are using and will directly authenticate with them. Your data is stored in a separate folder in your accounts on each of the storage providers.</p>
  </div>
  <div class="abs faq-item" style="top:408px">
    <h3>2 How do you ensure that no one else can see my data?</h3>
    <p>We use the latest in-browser AES-256 bit cipher to encrypt your files with a randomly generated key. Then your file contents are split and separate chunks are stored on the storage providers. This ensure that even if any of the storage providers gets hacked or compromised, all they will get is fragments of data that cannot be deciphered by even the most powerful computers, now or in the future.</p>
  </div>
  <div class="abs faq-item" style="top:564px">
    <h3>3 So does that mean I need to remember encryption keys for my files?</h3>
    <p>Nope. We believe you should have the freedom to not have to deal with encryption keys. The keys are themselves fragmented and stored on the storage providers in a patent-pending scheme that is automatically regenerated once you have authenticate yourself to all your storage providers.</p>
  </div>
  <div class="abs read-more">Read more</div>
</section>

<section class="abs developers">
  <h2>DEVELOPERS</h2>
  <p>If you are a developer and would like to create web applications that require the ability to store user data securely in the cloud, please drop us an email at developer@plimva.com. We are developing the REST and Javascript API that will enable you to do just that.</p>
</section>

<section class="abs contact">
  <h2>CONTACT US</h2>
  <p class="about">Plimva is based out of picturesque Larkmoor Falls, VT<br>We are a team of developers with a passion for building truly useful web applications that make our online lives easer and safer</p>
  <div class="abs social" style="left:48px" aria-label="Social link"></div>
  <div class="abs social" style="left:118px" aria-label="Social link"></div>
  <div class="abs social" style="left:188px" aria-label="Social link"></div>
  <div class="abs field" style="top:118px">Name</div>
  <div class="abs field" style="top:163px">Email</div>
  <div class="abs field" style="top:208px">Subject</div>
  <div class="abs message">Message</div>
  <div class="abs send">SEND</div>
  <div class="abs footer-rule"></div>
  <p class="abs copyright">© 2015 Venrell Technology LLC.</p>
</section>

</body>
</html>
```